Classic and neutral book cover design

We are looking for a classic and neutral book cover design to be used as the template for a series of books to be published. We are hence looking for a template that will allow us to easily change the title name for all books in this series.
The use of very few colours (black and white is welcome) and few design elements is a big bonus. As a source of inspiration we would like to ask you to view the very simple and
If you think you have a cool idea that can add a twist to the formal classic look don't hesitate. Go for it !
Work will be done for a 30 year old Sweden based cultural non-profit called VĂ©lra (www.velrafoundation.example). We work with the publishing and supporting of post-modern art and literature addressing contemporary topics but are also involved in assisting projects of cultural preservation.
Target Market(s)
The audience is expected to have some form of interest in culture but could range from hobbyist readers to tenure track scholars
Industry/Entity Type
Non-Profit
Requirements
Must have
- General:
- Classic and neutral feel
- Preferably very simple and few shapes
- usage of few colours (black and white is welcome)
Information to be displayed on the cover is:
- Author
- Title
- type of work e.g. play/novel (optional)
- publishing house (in this case "Velra Publishing")
Nice to have
- ideas to prevent it from become boring are of course welcome
Should not have
- - too many colours

```html
<!DOCTYPE html>
<html lang="en">
<head>
<meta charset="utf-8">
<title>Velra Publishing – Book Cover</title>
<link href="https://fonts.googleapis.com/css2?family=Crimson+Pro:ital,wght@0,400;1,400;1,500&display=swap" rel="stylesheet">
<style>
  :root {
    --paper: #ffffff;
    --ink: #0b0b0b;
  }
  html, body {
    margin: 0;
    padding: 0;
    background: var(--paper);
    overflow: hidden;
  }
  .cover {
    position: relative;
    width: 952px;
    height: 1200px;
    background: var(--paper);
    color: var(--ink);
    overflow: hidden;
    font-family: "Crimson Pro", "Times New Roman", serif;
  }
  .publisher {
    position: absolute;
    top: 179px;
    left: 0;
    width: 100%;
    text-align: center;
    font-style: italic;
    font-size: 18px;
    letter-spacing: 0.22em;
    text-transform: uppercase;
    margin: 0;
  }
  .title-art {
    position: absolute;
    top: 0;
    left: 0;
    width: 952px;
    height: 1200px;
  }
  .title-art text {
    font-family: "Crimson Pro", "Times New Roman", serif;
    font-style: italic;
    font-weight: 500;
    font-size: 272px;
    fill: var(--ink);
  }
  .work-type {
    position: absolute;
    top: 870px;
    left: 0;
    width: 100%;
    text-align: center;
    font-style: italic;
    font-size: 29px;
    margin: 0;
  }
  .byline {
    position: absolute;
    top: 927px;
    left: 0;
    width: 100%;
    text-align: center;
    font-style: italic;
    font-size: 17px;
    margin: 0;
  }
  .author {
    position: absolute;
    top: 958px;
    left: 0;
    width: 100%;
    text-align: center;
    font-size: 31px;
    letter-spacing: 0.17em;
    margin: 0;
  }
</style>
</head>
<body>
  <main class="cover">
    <p class="publisher">Velra Publishing</p>

    <svg class="title-art" viewBox="0 0 952 1200" aria-label="nice title">
      <text x="8 150 268 405" y="738 638 585 508" rotate="-22 -22 -22 -22">nice</text>
      <text x="400 518 622 740 852" y="752 679 620 554 488" rotate="-22 -22 -22 -22 -22">title</text>
    </svg>

    <p class="work-type">Novel</p>
    <p class="byline">by</p>
    <p class="author">Author Authorson</p>
  </main>
</body>
</html>
```